Playful Website Design Needed Pet Sitting and Dog Walking Business

Need a simple one page Web Design Built on WordPress.
Sections:

About Us
Services Provided
Costs
Contact Us
Intake Form (Questionnaire that goes to email)
See us in Action

Industry/Entity Type

Pet Sitting and Dog Walking

Number of Pages Required

1 page

Font styles to use
Other font styles liked:
• See the Business Card Font and use that.

Colors
EE7325
F08F49
F5BC92
FAE3D3
FDF4ED

Requirements
Must have
• See attached Logo Design, with Font's and Colors Use these as theme guide

```html
<!DOCTYPE html>
<html lang="en">
<head>
<meta charset="utf-8">
<title>Tailwag Companions – Pet Sitting &amp; Dog Walking</title>
<link href="https://fonts.googleapis.com/css2?family=Poppins:wght@300;400;500;600;700&display=swap" rel="stylesheet">
<style>
:root{
  --orange:#EE7325;
  --orange-bright:#FB7A2F;
  --orange-soft:#F08F49;
  --peach:#F5BC92;
  --cream:#FDF4ED;
  --green:#6DB33F;
  --green-deep:#5AA02E;
  --slate:#E7EAF1;
  --ink:#1F1F1F;
  --body:#3A3A3A;
  --white:#FFFFFF;
  --gray-bar:#E4E4E4;
}
*{box-sizing:border-box;margin:0;padding:0}
html,body{width:1200px;height:4289px;overflow:hidden}
body{position:relative;font-family:"Poppins",sans-serif;color:var(--body);background:var(--white)}
.abs{position:absolute}
.eyebrow{position:absolute;font-size:17px;letter-spacing:3px;text-transform:uppercase;color:var(--orange);font-weight:400}
.title{position:absolute;font-size:36px;font-weight:400;text-transform:uppercase;color:var(--ink);line-height:1.1}
.copy{position:absolute;font-size:13.5px;line-height:23.5px;color:var(--body)}
.btn{position:absolute;display:flex;align-items:center;justify-content:center;font-size:12.5px;font-weight:600;letter-spacing:1.5px;text-transform:uppercase;color:var(--white)}
.btn--orange{background:var(--orange)}
.btn--green{background:var(--green)}
.photo{position:absolute}

/* header */
.site-header{position:absolute;top:0;left:0;width:1200px;height:78px;background:var(--white);z-index:5}
.brand-plate{position:absolute;left:70px;top:0;width:245px;height:138px;z-index:6}
.brand{position:absolute;left:84px;top:34px;width:220px;z-index:7;display:flex;align-items:center;gap:8px}
.brand__dot{width:22px;height:22px;border-radius:50%;background:var(--green);flex:none}
.brand__name{font-size:21px;font-weight:600;color:var(--orange);line-height:1.05}
.nav{position:absolute;top:31px;left:356px;display:flex;font-size:13px;text-transform:uppercase;color:var(--ink);z-index:7}
.nav a{color:inherit;text-decoration:none;margin-right:42px}
.nav a.is-active{font-weight:600}
.nav__cta{position:absolute;left:958px;top:24px;width:148px;height:36px;background:var(--orange);color:var(--white);font-size:13px;text-transform:uppercase;display:flex;align-items:center;justify-content:center;z-index:7}

/* hero */
.hero{position:absolute;top:78px;left:0;width:1200px;height:640px}
.hero__title{position:absolute;top:108px;width:1200px;text-align:center;color:var(--white);line-height:1.12}
.hero__title span{display:block;font-size:42px;font-weight:300}
.hero__title strong{display:block;font-size:50px;font-weight:700}
.hero__lead{position:absolute;top:222px;left:395px;width:440px;text-align:center;color:var(--white);font-size:17px;line-height:25px;opacity:.92}

/* services */
.services{position:absolute;top:1248px;left:0;width:1200px;height:562px;background:var(--slate)}
.card{position:absolute;top:155px;width:326px;height:293px;box-shadow:0 2px 6px rgba(0,0,0,.15)}
.card__label{position:absolute;left:10px;right:10px;top:211px;height:72px;display:flex;flex-direction:column;align-items:center;justify-content:center;color:var(--white)}
.card__label b{font-size:17px;font-weight:600;letter-spacing:2px;text-transform:uppercase}
.card__label small{font-size:10.5px;letter-spacing:1.5px;text-transform:uppercase;opacity:.85;margin-top:4px}

/* contact */
.info-row{position:absolute;display:flex;align-items:center;gap:14px;color:var(--white)}
.info-row__icon{width:58px;height:58px;border-radius:50%;background:var(--white);display:flex;align-items:center;justify-content:center}
.info-row small{display:block;font-size:13px;opacity:.9}
.info-row b{display:block;font-size:17px;font-weight:600}

/* form */
.field{position:absolute;background:var(--white);font-size:13px;color:var(--ink);padding:16px 20px}

/* footer */
.footer-col{position:absolute;top:4030px}
.footer-col h4{font-size:15px;font-weight:600;color:var(--orange);letter-spacing:1px;text-transform:uppercase}
.footer-col h4::after{content:"";display:block;width:52px;height:2px;background:var(--orange);margin-top:6px}
.footer-col ul{list-style:none;margin-top:14px}
.footer-col li{font-size:11px;line-height:22px;color:var(--body)}
.footer-contact{position:absolute;display:flex;align-items:center;gap:12px;font-size:11px;line-height:18px;color:var(--body)}
.footer-contact__icon{width:32px;height:32px;border-radius:50%;background:var(--green);display:flex;align-items:center;justify-content:center}
.copyright{position:absolute;top:4235px;left:0;width:1200px;height:54px;background:var(--gray-bar);display:flex;align-items:center;justify-content:center;font-size:10px;color:var(--body)}
</style>
</head>
<body>

<!-- HEADER -->
<header class="site-header">
  <nav class="nav">
    <a class="is-active" href="#about">About Us</a>
    <a href="#services">Services Provided</a>
    <a href="#costs">Costs</a>
    <a href="#contact">Contact Us</a>
    <a href="#intake">Intake Form</a>
  </nav>
  <div class="nav__cta">See Us In Action</div>
</header>
<svg class="brand-plate" viewBox="0 0 245 138" aria-hidden="true">
  <path d="M0 0 H245 V60 C245 110 190 138 122 138 C55 138 0 110 0 60 Z" fill="#fff"/>
</svg>
<div class="brand"><span class="brand__dot"></span><span class="brand__name">Tailwag<br>Companions</span></div>

<!-- HERO -->
<section class="hero">
  <svg class="abs" style="left:0;top:0" width="1200" height="640" viewBox="0 0 1200 640" role="img" aria-label="Photo of a group of leashed dogs with walkers on a city street, tinted orange">
    <defs>
      <linearGradient id="heroTone" x1="0" y1="0" x2="0" y2="1">
        <stop offset="0" stop-color="#EE6A1E"/>
        <stop offset=".55" stop-color="#C9571F"/>
        <stop offset="1" stop-color="#6E3A22"/>
      </linearGradient>
    </defs>
    <rect width="1200" height="640" fill="url(#heroTone)"/>
    <path d="M0 630 C200 600 420 640 640 615 C860 590 1050 560 1200 560 V640 H0 Z" fill="#fff"/>
    <path d="M0 630 C200 600 420 640 640 615 C860 590 1050 560 1200 552" fill="none" stroke="#EE7325" stroke-width="6"/>
  </svg>
  <h1 class="hero__title"><span>WELCOME TO</span><strong>TAILWAG COMPANIONS</strong></h1>
  <p class="hero__lead">Lorem ipsum dolor sit amet, consectetur adipiscing elit, sed do eiusmod tempor incididu</p>
  <div class="btn btn--green" style="left:536px;top:288px;width:173px;height:43px;font-size:15px;letter-spacing:.5px">Learn More</div>
</section>

<!-- ABOUT -->
<section id="about">
  <svg class="abs" style="left:100px;top:782px" width="300" height="200" aria-hidden="true">
    <path d="M300 0 H40 A40 40 0 0 0 0 40 V200 H22 V42 A20 20 0 0 1 42 22 H300 Z" fill="#6DB33F"/>
  </svg>
  <div class="photo" role="img" aria-label="Photo of a smiling woman kneeling with four brown hounds outdoors" style="left:122px;top:804px;width:482px;height:357px;background:linear-gradient(135deg,#3E5A2E,#7A4A2A 55%,#A9683E);border-radius:0 0 28px 0"></div>
  <div class="eyebrow" style="left:669px;top:818px">Who We Are</div>
  <h2 class="title" style="left:669px;top:842px">About Pet Sitting</h2>
  <p class="copy" style="left:669px;top:897px;width:452px">Lorem ipsum dolor sit amet, consectetur adipiscing elit, sed do eiusmod tempor incididunt ut labore et dolore magna aliqua. Ut enim ad minim veniam, quis nostrud exercitation ullamco laboris nisi ut aliquip ex ea commodo consequat.</p>
  <p class="copy" style="left:669px;top:1003px;width:452px">Duis aute irure dolor in reprehenderit in voluptate velit esse cillum dolore eu fugiat nulla pariatur. Excepteur sint occaecat cupidatat non proident, sunt in culpa qui officia deserunt mollit</p>
  <div class="btn btn--orange" style="left:672px;top:1097px;width:162px;height:40px">Learn More</div>
</section>

<!-- SERVICES -->
<section id="services" class="services">
  <div class="eyebrow" style="left:0;width:1200px;text-align:center;top:68px">What We Do</div>
  <h2 class="title" style="left:0;width:1200px;text-align:center;top:90px">Our Services</h2>

  <div class="card" style="left:101px" role="img" aria-label="Photo of beagle puppies eating from green bowls">
    <div class="abs" style="inset:0;background:linear-gradient(160deg,#CFC7BE,#8A7A6A 70%,#5C4E44)"></div>
    <div class="card__label" style="background:rgba(238,115,37,.92)"><b>Feed Service</b><small>Learn More</small></div>
  </div>
  <div class="card" style="left:445px" role="img" aria-label="Photo of two people petting a group of dogs on a city street">
    <div class="abs" style="inset:0;background:linear-gradient(160deg,#6F6A63,#3F3A35 60%,#8C7A66)"></div>
    <div class="card__label" style="background:rgba(238,115,37,.92)"><b>Walk &amp; Play With Pet</b><small>Learn More</small></div>
  </div>
  <div class="card" style="left:792px" role="img" aria-label="Photo of a woman crouching to greet a shiba inu dog outdoors">
    <div class="abs" style="inset:0;background:linear-gradient(160deg,#5E4636,#8F6A4E 55%,#B89A82)"></div>
    <div class="card__label" style="background:rgba(109,179,63,.9)"><b>Each Visit</b><small>Learn More</small></div>
  </div>
</section>

<!-- PRICING -->
<section id="costs">
  <div class="eyebrow" style="left:122px;top:1906px">Costs</div>
  <h2 class="title" style="left:122px;top:1928px">Our Pricing</h2>
  <p class="copy" style="left:122px;top:1982px;width:338px;font-size:12.5px;line-height:23.5px">Lorem ipsum dolor sit amet, consectetur adipiscing elit, sed do eiusmod tempor incididunt ut labore et dolore magna aliqua. Ut enim ad minim veniam, quis nostrud exercitation ullamco laboris nisi ut aliquip ex ea commodo consequat.</p>
  <div class="abs" style="left:125px;top:2112px;font-size:19px;font-weight:500;color:var(--orange)">$8 per visit. 2 visit a day</div>
  <div class="btn btn--green" style="left:127px;top:2164px;width:163px;height:41px">Learn More</div>
  <svg class="abs" style="left:330px;top:2158px" width="115" height="42" viewBox="0 0 115 42" aria-hidden="true">
    <path d="M4 6 C20 38 70 40 104 14" fill="none" stroke="#EE7325" stroke-width="2" stroke-dasharray="4 4"/>
    <path d="M94 10 L108 10 L102 22" fill="none" stroke="#EE7325" stroke-width="2.5"/>
  </svg>
  <div class="photo" role="img" aria-label="Photo of a large group of dogs of many breeds sitting together" style="left:455px;top:1930px;width:690px;height:300px;background:radial-gradient(ellipse at 50% 60%,#B9946E 0%,#8B6A4C 40%,rgba(255,255,255,0) 72%)"></div>
</section>

<!-- CONTACT -->
<section id="contact">
  <svg class="abs" style="left:0;top:2290px" width="1200" height="595" viewBox="0 0 1200 595" aria-hidden="true">
    <path d="M0 8 C160 60 330 40 600 40 C860 40 1040 40 1200 0 V595 H0 Z" fill="#FB7A2F"/>
  </svg>
  <svg class="abs" style="left:112px;top:2380px" width="450" height="450" viewBox="0 0 450 450" role="img" aria-label="Photo of dog walkers with several dogs in a sunny park, with an inset of a person holding a shiba inu">
    <defs>
      <linearGradient id="parkTone" x1="0" y1="0" x2="1" y2="1">
        <stop offset="0" stop-color="#E8B06A"/><stop offset=".5" stop-color="#A8763E"/><stop offset="1" stop-color="#6A4A30"/>
      </linearGradient>
    </defs>
    <circle cx="222" cy="224" r="221" fill="none" stroke="#fff" stroke-width="2"/>
    <circle cx="222" cy="224" r="208" fill="url(#parkTone)" stroke="#fff" stroke-width="6"/>
    <circle cx="379" cy="357" r="83" fill="#7A9AA8" stroke="#fff" stroke-width="5"/>
  </svg>
  <div class="eyebrow" style="left:627px;top:2448px;color:var(--white)">Get In Touch</div>
  <h2 class="title" style="left:627px;top:2470px;color:var(--white)">Contact Us</h2>
  <p class="copy" style="left:627px;top:2520px;width:390px;color:var(--white);font-size:14.5px;line-height:25px">Lorem ipsum dolor sit amet, consectetur adipiscing elit, sed do eiusmod tempor incididunt</p>
  <div class="info-row" style="left:627px;top:2595px">
    <span class="info-row__icon"><svg width="26" height="26" viewBox="0 0 24 24" aria-hidden="true"><path d="M6.6 10.8a15.5 15.5 0 0 0 6.6 6.6l2.2-2.2a1 1 0 0 1 1-.25 11.4 11.4 0 0 0 3.6.6 1 1 0 0 1 1 1V20a1 1 0 0 1-1 1A17 17 0 0 1 3 4a1 1 0 0 1 1-1h3.5a1 1 0 0 1 1 1c0 1.25.2 2.45.6 3.6a1 1 0 0 1-.25 1Z" fill="#FB7A2F"/></svg></span>
    <span><small>Phone Number</small><b>(555) 014-2290</b></span>
  </div>
  <div class="info-row" style="left:627px;top:2672px">
    <span class="info-row__icon"><svg width="26" height="22" viewBox="0 0 24 20" aria-hidden="true"><rect x="1" y="2" width="22" height="16" rx="2" fill="#FB7A2F"/><path d="M2 4 L12 11 L22 4" fill="none" stroke="#fff" stroke-width="2"/></svg></span>
    <span><small>Email address</small><b style="font-size:15px">hello@tailwagcompanions.com</b></span>
  </div>
</section>

<!-- INTAKE FORM -->
<section id="intake">
  <svg class="abs" style="left:0;top:2879px" width="1200" height="490" viewBox="0 0 1200 490" role="img" aria-label="Photo of colourful dog toys and bowls on a green surface">
    <defs>
      <radialGradient id="toyTone" cx=".5" cy=".45" r=".7">
        <stop offset="0" stop-color="#8CC84B"/><stop offset="1" stop-color="#5E9E2C"/>
      </radialGradient>
    </defs>
    <rect width="1200" height="490" fill="url(#toyTone)"/>
    <path d="M0 490 V470 C200 460 320 420 600 440 C850 458 1000 420 1200 400 V490 Z" fill="#F3F1EC"/>
  </svg>
  <div class="abs" style="left:0;top:2938px;width:1200px;text-align:center;font-size:13px;letter-spacing:2px;color:var(--white)">BOOK NOW</div>
  <h2 class="title" style="left:0;top:2958px;width:1230px;text-align:center;color:var(--white);font-size:33px">Contact Form</h2>
  <div class="field" style="left:226px;top:3029px;width:371px;height:46px">Name</div>
  <div class="field" style="left:226px;top:3087px;width:371px;height:46px">Email address</div>
  <div class="field" style="left:226px;top:3143px;width:371px;height:47px">Phone</div>
  <div class="field" style="left:607px;top:3029px;width:370px;height:161px">Message</div>
  <div class="btn btn--orange" style="left:508px;top:3211px;width:179px;height:39px;font-size:13.5px">Submit Now</div>
</section>

<!-- SEE US IN ACTION -->
<section id="action">
  <div class="abs" style="left:0;top:3361px;width:1200px;height:608px;background:linear-gradient(180deg,#F3F1EC,#FAFAF8 70%,#F0EEEA)"></div>
  <div class="eyebrow" style="left:135px;top:3518px;font-size:19px">Dog Care</div>
  <h2 class="title" style="left:133px;top:3544px;font-size:40px">See Us In Action</h2>
  <p class="copy" style="left:135px;top:3602px;width:410px;font-size:15.5px;line-height:28px">Lorem ipsum dolor sit amet, consectetur adipiscing elit, sed do eiusmod tempor incididunt ut labore et dolore magna aliqua.</p>
  <div class="btn btn--orange" style="left:140px;top:3719px;width:168px;height:42px">Learn More</div>
  <svg class="abs" style="left:345px;top:3710px" width="120" height="50" viewBox="0 0 120 50" aria-hidden="true">
    <path d="M4 10 C20 46 74 48 108 16" fill="none" stroke="#EE7325" stroke-width="2" stroke-dasharray="4 4"/>
    <path d="M98 12 L112 12 L106 24" fill="none" stroke="#EE7325" stroke-width="2.5"/>
  </svg>
  <svg class="abs" style="left:570px;top:3420px" width="490" height="490" viewBox="0 0 490 490" role="img" aria-label="Photo of three dog walkers leading a pack of dogs along a tree-lined path">
    <defs>
      <linearGradient id="pathTone" x1="0" y1="0" x2="0" y2="1">
        <stop offset="0" stop-color="#5E8A3A"/><stop offset=".55" stop-color="#7C7060"/><stop offset="1" stop-color="#A39A8E"/>
      </linearGradient>
    </defs>
    <path d="M245 4 A241 241 0 0 1 486 245" fill="none" stroke="#EE7325" stroke-width="10"/>
    <path d="M245 486 A241 241 0 0 1 4 245" fill="none" stroke="#6DB33F" stroke-width="10"/>
    <path d="M486 245 A241 241 0 0 1 245 486" fill="none" stroke="#EE7325" stroke-width="10"/>
    <circle cx="245" cy="245" r="226" fill="url(#pathTone)"/>
  </svg>
</section>

<!-- FOOTER -->
<footer>
  <div class="brand" style="top:4080px;left:113px;width:200px"><span class="brand__dot"></span><span class="brand__name">Tailwag<br>Companions</span></div>

  <div class="footer-col" style="left:383px">
    <h4>Quick Links</h4>
    <ul><li>Home</li><li>About Us</li><li>Costs</li><li>Service Provided</li><li>Contact Us</li></ul>
  </div>
  <div class="footer-col" style="left:603px">
    <h4>Resources</h4>
    <ul><li>Intake Form</li><li>Why Choose Us</li><li>Gallery</li><li>Terms of Use</li><li>Privacy Policy</li></ul>
  </div>
  <div class="footer-col" style="left:818px">
    <h4>Contact Us</h4>
  </div>
  <div class="footer-contact" style="left:820px;top:4076px">
    <span class="footer-contact__icon"><svg width="15" height="15" viewBox="0 0 24 24" aria-hidden="true"><path d="M6.6 10.8a15.5 15.5 0 0 0 6.6 6.6l2.2-2.2a1 1 0 0 1 1-.25 11.4 11.4 0 0 0 3.6.6 1 1 0 0 1 1 1V20a1 1 0 0 1-1 1A17 17 0 0 1 3 4a1 1 0 0 1 1-1h3.5a1 1 0 0 1 1 1c0 1.25.2 2.45.6 3.6a1 1 0 0 1-.25 1Z" fill="#fff"/></svg></span>
    <span>Phone Number<br>(555) 014-2290</span>
  </div>
  <div class="footer-contact" style="left:820px;top:4133px">
    <span class="footer-contact__icon"><svg width="15" height="13" viewBox="0 0 24 20" aria-hidden="true"><rect x="1" y="2" width="22" height="16" rx="2" fill="#fff"/><path d="M2 4 L12 11 L22 4" fill="none" stroke="#6DB33F" stroke-width="2"/></svg></span>
    <span>Email address<br>hello@tailwagcompanions.com</span>
  </div>
  <div class="copyright">© 2022 Company Name | All Rights Reserved</div>
</footer>

</body>
</html>
```